Chiropractic Business Card

I need a business card designed to help me stand apart from my competition. I really like simple, clean designs that appear open and inviting. I would like the designs to incorporate the color blue, green, or both. I really like the attached picture because it highlights that I just don't treat "back pain" and it being a nice computer graphic helps show that I have a modern practice. "Modern practice" meaning merging technology and most current research in my patient care.

My information is:

Wesley Marrin, DC
Phone- (707) 555-0182
Email- drwesleymarrin@example-mail.net
Website- www.pelhamchiropractic.example
Address- 248 Tolliver Street, Sonoma, CA 95476

Jpeg and pdf attached of Pelham Chiropractic logo.
Updates

Atmosphere to be clean lines and solid colors to be have gradient fading, but don't want too much going on with the fading. Simple.

Target Market(s)

Active adults who are health conscious between the ages of 20-70

Industry/Entity Type

Computer

Colors
0455a3
85cae6

Requirements
Must have
• Change color of Pelham chiropractic logo (maroon) to fit the rest of the design.
Nice to have
• Can separate the running image from the black background to have it work with the design.

```html
<!DOCTYPE html>
<html lang="en">
<head>
<meta charset="UTF-8">
<title>Pelham Chiropractic – Business Card</title>
<link href="https://fonts.googleapis.com/css2?family=Josefin+Sans:wght@400;600&family=Playfair+Display:wght@700&display=swap" rel="stylesheet">
<style>
  :root {
    --bg: #e6e5e1;
    --card: #f7f7f6;
    --ink: #4a4a4a;
    --rule: #9a9a9a;
    --green: #6aa532;
    --blue: #1f56a0;
    --figure-a: #7fa6c4;
    --figure-b: #3d6d96;
  }
  * { box-sizing: border-box; margin: 0; padding: 0; }
  html, body { width: 1200px; height: 900px; overflow: hidden; background: var(--bg); }
  .canvas { position: relative; width: 1200px; height: 900px; }
  .card {
    position: absolute; left: 280px; width: 640px; height: 366px;
    background: var(--card); overflow: hidden;
    box-shadow: 0 6px 18px rgba(0,0,0,.18);
    font-family: "Josefin Sans", sans-serif; color: var(--ink);
  }
  .card--front { top: 48px; }
  .card--back { top: 478px; }

  .brand {
    font-family: "Playfair Display", serif; font-weight: 700;
    color: var(--green); letter-spacing: 1px; line-height: 1;
    text-transform: uppercase; white-space: nowrap;
  }
  .card--front .brand { position: absolute; left: 368px; top: 164px; font-size: 27px; }
  .card--front .brand-mark {
    position: absolute; left: 342px; top: 168px; width: 16px; height: 16px;
    border-radius: 50%; background: var(--green);
  }
  .runner-art {
    position: absolute; left: 70px; top: 24px; width: 250px; height: 320px;
    border-radius: 40% 45% 30% 35%;
    background: radial-gradient(circle at 40% 60%, rgba(220,70,70,.45) 0 10%, transparent 22%),
                linear-gradient(160deg, var(--figure-a), var(--figure-b));
    opacity: .85;
  }

  .card--back .brand { position: absolute; left: 372px; top: 50px; font-size: 25px; }
  .card--back .brand-mark {
    position: absolute; left: 348px; top: 54px; width: 15px; height: 15px;
    border-radius: 50%; background: var(--green);
  }
  .holder { position: absolute; left: 40px; top: 48px; width: 280px; }
  .holder-name { font-size: 14px; font-weight: 600; letter-spacing: 3px; text-transform: uppercase; }
  .holder-address { margin-top: 18px; font-size: 11px; letter-spacing: 2px; line-height: 1.9; text-transform: uppercase; }
  .divider { position: absolute; left: 40px; right: 40px; top: 166px; height: 1px; background: var(--rule); }
  .contact { position: absolute; right: 40px; top: 236px; text-align: right; font-size: 12px; letter-spacing: 2px; }
  .contact-row { display: flex; align-items: center; justify-content: flex-end; gap: 10px; height: 24px; }
  .contact-row + .contact-row { border-top: 1px solid var(--rule); }
  .contact-row svg { width: 14px; height: 14px; fill: var(--blue); flex: none; }
  .band-blue { position: absolute; left: 0; bottom: 0; width: 220px; height: 8px; background: var(--blue); }
  .band-green {
    position: absolute; left: 190px; right: 0; bottom: 0; height: 40px;
    background: var(--green); border-top-left-radius: 40px 40px;
    display: flex; align-items: center; padding-left: 44px;
  }
  .website { color: #fff; font-size: 13px; font-weight: 600; letter-spacing: 3px; text-transform: uppercase; white-space: nowrap; }
</style>
</head>
<body>
<main class="canvas">
  <section class="card card--front">
    <div class="runner-art" role="img" aria-label="Computer illustration of a running figure with highlighted joints"></div>
    <span class="brand-mark"></span>
    <div class="brand">Pelham<br>Chiropractic</div>
  </section>

  <section class="card card--back">
    <div class="holder">
      <div class="holder-name">Wesley Marrin, DC</div>
      <div class="holder-address">Address: 248 Tolliver Street<br>Halvern CA 95012</div>
    </div>
    <span class="brand-mark"></span>
    <div class="brand">Pelham<br>Chiropractic</div>
    <div class="divider"></div>
    <div class="contact">
      <div class="contact-row">(707) 555-0182
        <svg viewBox="0 0 24 24"><path d="M6.6 10.8a15.1 15.1 0 0 0 6.6 6.6l2.2-2.2a1 1 0 0 1 1-.25 11.4 11.4 0 0 0 3.6.57 1 1 0 0 1 1 1V20a1 1 0 0 1-1 1A17 17 0 0 1 3 4a1 1 0 0 1 1-1h3.5a1 1 0 0 1 1 1c0 1.25.2 2.45.57 3.6a1 1 0 0 1-.25 1z"/></svg>
      </div>
      <div class="contact-row">drwesleymarrin@example-mail.net
        <svg viewBox="0 0 24 24"><path d="M3 5h18a1 1 0 0 1 1 1v12a1 1 0 0 1-1 1H3a1 1 0 0 1-1-1V6a1 1 0 0 1 1-1zm0 2v.4l9 5.6 9-5.6V7l-9 5.6z"/></svg>
      </div>
    </div>
    <div class="band-blue"></div>
    <div class="band-green"><span class="website">www.pelhamchiropractic.example</span></div>
  </section>
</main>
</body>
</html>
```